Kesta furniture

A single page e commerce website for a new furniture company.

The opening range would consist of 3 collections - Each collection would consist of a bed , sofa & arm chair.

So total 9 items.

We would want a single page which has the 3 collections on it which are available to purchase from the website.

See attached the logo & branding for colours

Target Market(s)

customers wanting to buy high end furniture

Industry/Entity Type

furniture retail

Coding

Coded - Design and coding required

Number of Pages Required

1 page

Colors
00AB8E
00BBA5
67D7C9
C6EFE9
E9F9F6

```html
<!DOCTYPE html>
<html lang="en">
<head>
<meta charset="utf-8">
<title>Kesta furniture</title>
<link rel="stylesheet" href="https://fonts.googleapis.com/css2?family=Questrial&display=swap">
<style>
:root{
  --teal:#0fa6b4;
  --teal-dark:#0b8f9c;
  --ink:#222;
  --muted:#666;
  --card:#ececec;
  --footer:#ececec;
  --white:#fff;
}
*{box-sizing:border-box;margin:0;padding:0}
html,body{width:1200px;height:4292px;overflow:hidden}
body{position:relative;background:var(--white);font-family:"Questrial",sans-serif;color:var(--ink)}
.abs{position:absolute}

/* header */
.site-header{left:0;top:0;width:1200px;height:112px;background:var(--white)}
.brand{left:152px;top:0;width:168px;height:200px;background:var(--teal);color:var(--white);
  display:flex;align-items:center;justify-content:center;text-align:center;font-size:30px;line-height:1.15;z-index:3;padding:0 14px}
.search{left:660px;top:20px;width:240px;height:34px;border:1.5px solid #bbb;border-radius:18px;font-size:15px;color:#999;padding:7px 16px}
.search svg{position:absolute;right:12px;top:7px}
.icons{left:925px;top:22px;display:flex;gap:20px}
.cart-badge{position:absolute;right:-8px;top:-6px;width:14px;height:14px;border-radius:50%;background:var(--teal);color:#fff;font-size:9px;text-align:center;line-height:14px}
.nav{left:468px;top:70px;display:flex;gap:36px;font-size:15px;text-transform:uppercase}
.nav a{color:var(--ink);text-decoration:none}
.nav a.active{border-bottom:2px solid var(--ink);padding-bottom:3px}

/* hero */
.hero{left:0;top:112px;width:1200px;height:608px;
  background:linear-gradient(180deg,rgba(0,0,0,.05),rgba(0,0,0,.2)),
  radial-gradient(ellipse at 55% 60%,#3f7d88 0 18%,transparent 40%),
  linear-gradient(90deg,#a79c8a 0%,#6f8a90 30%,#58767e 60%,#cfd3d0 85%,#e8e6e0 100%)}
.hero-floor{left:0;top:600px;width:1200px;height:120px;background:linear-gradient(180deg,#8a6a4f,#5e4532)}
.hero-title{left:152px;top:352px;color:var(--white);font-size:46px;line-height:1.1;text-transform:uppercase;letter-spacing:1px;font-weight:400}
.btn{display:inline-block;background:var(--teal);color:var(--white);text-transform:uppercase;font-size:14px;text-align:center}
.hero-btn{left:152px;top:488px;width:112px;height:40px;line-height:40px}

/* collections */
.section-title{left:0;width:1200px;text-align:center;font-size:40px;text-transform:uppercase;font-weight:400}
.section-title::after{content:"";display:block;width:60px;height:3px;background:var(--teal);margin:16px auto 0}
.card{width:372px;height:268px;background:var(--card);border-radius:6px}
.card .product{position:absolute;left:60px;top:20px;width:252px;height:160px;border-radius:8px}
.card .name{position:absolute;left:24px;top:204px;font-size:15px;text-transform:uppercase}
.card .desc{position:absolute;left:24px;top:224px;font-size:11px;color:var(--muted)}
.card .btn{position:absolute;right:24px;top:204px;width:92px;height:36px;line-height:36px;font-size:13px;text-transform:none}

/* video */
.video{left:0;top:2240px;width:1200px;height:452px;
  background:linear-gradient(180deg,#d9d6d0 0%,#c9c6c0 45%,#9a9c9c 65%,#bfbcb6 100%)}
.play{left:545px;top:2411px}

/* instagram */
.insta{width:288px;height:268px;border-radius:6px}

/* testimonial */
.testimonial{left:0;top:3500px;width:1200px;height:328px;background:var(--teal);color:var(--white);text-align:center}
.quote-mark{left:0;top:3556px;width:1200px;text-align:center;font-size:80px;line-height:1;color:#fff}
.quote-text{left:220px;top:3644px;width:760px;font-size:17px;line-height:1.5;color:#fff;text-align:center}
.quote-name{left:0;top:3750px;width:1200px;text-align:center;font-size:17px;color:#fff}
.stars{left:0;top:3780px;width:1200px;text-align:center;color:#f6c445;font-size:16px;letter-spacing:2px}
.arrow{top:3640px}

/* footer */
.site-footer{left:0;top:3828px;width:1200px;height:464px;background:var(--footer)}
.footer-brand{left:152px;top:3940px;width:188px;height:192px;background:var(--teal);color:var(--white);
  display:flex;align-items:center;justify-content:center;text-align:center;font-size:30px;line-height:1.15;padding:0 14px}
.foot-title{font-size:24px}
.links{left:400px;top:3920px}
.links ul{list-style:none;margin-top:22px;font-size:15px;line-height:24px}
.contact{left:588px;top:3920px}
.contact-row{display:flex;gap:14px;align-items:flex-start;font-size:13px;line-height:18px;margin-top:14px}
.contact-row:first-of-type{margin-top:20px}
.dot{flex:none;width:34px;height:34px;border-radius:50%;background:var(--teal);display:flex;align-items:center;justify-content:center}
.newsletter{left:840px;top:3920px;width:260px}
.newsletter p{font-size:13px;color:var(--muted);margin-top:14px;line-height:18px}
.email{position:relative;margin-top:14px;width:260px;height:40px;border-radius:20px;background:var(--white);font-size:14px;padding:11px 18px}
.email .go{position:absolute;right:3px;top:3px;width:34px;height:34px;border-radius:50%;background:var(--teal);display:flex;align-items:center;justify-content:center}
.social{display:flex;gap:8px;margin-top:18px}
.social span{width:30px;height:30px;border-radius:50%;border:1.5px solid #444}
.bottom-bar{left:0;top:4232px;width:1200px;height:60px;border-top:1px solid #d6d6d6}
.copyright{left:152px;top:4256px;font-size:13px}
.payments{left:850px;top:4250px;display:flex;gap:8px}
.payments span{width:40px;height:24px;border-radius:3px;background:#c9c9c9}
</style>
</head>
<body>

<header class="abs site-header">
  <div class="abs search">Search
    <svg width="18" height="18" viewBox="0 0 18 18"><circle cx="7.5" cy="7.5" r="5.5" fill="none" stroke="#555" stroke-width="1.6"/><line x1="11.5" y1="11.5" x2="16" y2="16" stroke="#555" stroke-width="1.6"/></svg>
  </div>
  <div class="abs icons">
    <svg width="22" height="22" viewBox="0 0 22 22"><circle cx="11" cy="7" r="4.5" fill="none" stroke="#333" stroke-width="1.5"/><path d="M3 20c1-5 15-5 16 0" fill="none" stroke="#333" stroke-width="1.5"/></svg>
    <svg width="22" height="22" viewBox="0 0 22 22"><path d="M11 19S2 13 2 7.5A4.5 4.5 0 0 1 11 5a4.5 4.5 0 0 1 9 2.5C20 13 11 19 11 19z" fill="none" stroke="#333" stroke-width="1.5"/></svg>
    <span style="position:relative"><svg width="24" height="22" viewBox="0 0 24 22"><path d="M1 2h4l3 12h12l2-8H7" fill="none" stroke="#333" stroke-width="1.5"/><circle cx="10" cy="18" r="1.8" fill="#333"/><circle cx="18" cy="18" r="1.8" fill="#333"/></svg><span class="cart-badge">0</span></span>
  </div>
  <nav class="abs nav">
    <a class="active" href="#">Home</a>
    <a href="#">Furniture Collections</a>
    <a href="#">About Us</a>
    <a href="#">Blog</a>
    <a href="#">Contact</a>
  </nav>
</header>
<div class="abs brand">Kesta furniture</div>

<section>
  <div class="abs hero" role="img" aria-label="Living room with a teal corner sofa, floor lamp and gold pendant lights"></div>
  <div class="abs hero-floor" role="img" aria-label="Wooden floor"></div>
  <h1 class="abs hero-title">Welcome to<br>Kesta furniture</h1>
  <a class="abs btn hero-btn">Buy Now</a>
</section>

<h2 class="abs section-title" style="top:806px">Collection 1</h2>
<div class="abs card" style="left:20px;top:892px">
  <div class="product" role="img" aria-label="Cream upholstered bed" style="background:linear-gradient(180deg,#ece9e2,#d9d5cc)"></div>
  <div class="name">Bed Collections</div><div class="desc">Lorem ipsum dolor sit amet</div><a class="btn">Shop Now</a>
</div>
<div class="abs card" style="left:414px;top:892px">
  <div class="product" role="img" aria-label="Tufted beige chesterfield sofa" style="background:linear-gradient(180deg,#e4ddd1,#c9bea9)"></div>
  <div class="name">Sofa Collections</div><div class="desc">Lorem ipsum dolor sit amet</div><a class="btn">Shop Now</a>
</div>
<div class="abs card" style="left:808px;top:892px">
  <div class="product" role="img" aria-label="White curved arm chair" style="background:linear-gradient(180deg,#f2f2f2,#d8d8d8)"></div>
  <div class="name">Arm Chair</div><div class="desc">Lorem ipsum dolor sit amet</div><a class="btn">Shop Now</a>
</div>

<h2 class="abs section-title" style="top:1290px">Collection 2</h2>
<div class="abs card" style="left:20px;top:1380px">
  <div class="product" role="img" aria-label="Dark bed with blue bedding" style="background:linear-gradient(180deg,#5d6670,#2f4f86)"></div>
  <div class="name">Bed Collections</div><div class="desc">Lorem ipsum dolor sit amet</div><a class="btn">Shop Now</a>
</div>
<div class="abs card" style="left:414px;top:1380px">
  <div class="product" role="img" aria-label="Light turquoise sofa" style="background:linear-gradient(180deg,#8fd8e6,#4fb8cc)"></div>
  <div class="name">Sofa Collections</div><div class="desc">Lorem ipsum dolor sit amet</div><a class="btn">Shop Now</a>
</div>
<div class="abs card" style="left:808px;top:1380px">
  <div class="product" role="img" aria-label="Teal wingback arm chair" style="background:linear-gradient(180deg,#2a8a94,#12626c)"></div>
  <div class="name">Arm Chair</div><div class="desc">Lorem ipsum dolor sit amet</div><a class="btn">Shop Now</a>
</div>

<h2 class="abs section-title" style="top:1778px">Collection 3</h2>
<div class="abs card" style="left:20px;top:1868px">
  <div class="product" role="img" aria-label="Dark grey platform bed" style="background:linear-gradient(180deg,#4a4644,#d9d6d2)"></div>
  <div class="name">Bed Collections</div><div class="desc">Lorem ipsum dolor sit amet</div><a class="btn">Shop Now</a>
</div>
<div class="abs card" style="left:414px;top:1868px">
  <div class="product" role="img" aria-label="Grey fabric sofa with yellow cushion" style="background:linear-gradient(180deg,#8a8784,#5f5c5a)"></div>
  <div class="name">Sofa Collections</div><div class="desc">Lorem ipsum dolor sit amet</div><a class="btn">Shop Now</a>
</div>
<div class="abs card" style="left:808px;top:1868px">
  <div class="product" role="img" aria-label="Black tufted leather arm chair" style="background:linear-gradient(180deg,#3a3a3a,#151515)"></div>
  <div class="name">Arm Chair</div><div class="desc">Lorem ipsum dolor sit amet</div><a class="btn">Shop Now</a>
</div>

<div class="abs video" role="img" aria-label="Video still of a grey sofa with cushions and a plant in a bright room"></div>
<svg class="abs play" width="110" height="110" viewBox="0 0 110 110"><circle cx="55" cy="55" r="50" fill="rgba(255,255,255,.15)" stroke="#fff" stroke-width="6"/><path d="M44 34v42l34-21z" fill="#fff"/></svg>

<h2 class="abs section-title" style="top:2796px">Folow us Instagram</h2>
<div class="abs insta" style="left:148px;top:2888px;background:linear-gradient(135deg,#5b4a3e,#b88a5e)" role="img" aria-label="Bedroom with wooden bed"></div>
<div class="abs insta" style="left:456px;top:2888px;background:linear-gradient(135deg,#cfd7d2,#7f9a86)" role="img" aria-label="Sofa with plants"></div>
<div class="abs insta" style="left:764px;top:2888px;background:linear-gradient(135deg,#2e3a4c,#a8b4c4)" role="img" aria-label="Couple relaxing on a sofa"></div>
<div class="abs insta" style="left:148px;top:3180px;background:linear-gradient(135deg,#eeeae4,#c96f45)" role="img" aria-label="Orange chairs by a window"></div>
<div class="abs insta" style="left:456px;top:3180px;background:linear-gradient(135deg,#a08a74,#e6e8ec)" role="img" aria-label="Mattress in a room"></div>
<div class="abs insta" style="left:764px;top:3180px;background:linear-gradient(135deg,#f0efec,#b9b6b1)" role="img" aria-label="Grey sofa in a white room"></div>

<section class="abs testimonial"></section>
<div class="abs quote-mark">&#8220;</div>
<p class="abs quote-text">Sed ut perspiciatis unde omnis iste natus error sit voluptatem accusantium doloremque laudantium, totam rem aperiam, eaque ipsa quae ab illo inventore veritatis et quasi ar chitecto beatae vitae dicta sunt explicabo nemo enim ipsam voluptatem quia</p>
<div class="abs quote-name">Mara Lindqvist</div>
<div class="abs stars">&#9733;&#9733;&#9733;&#9733;&#9733;</div>
<svg class="abs arrow" style="left:112px" width="24" height="40" viewBox="0 0 24 40"><path d="M20 4L6 20l14 16" fill="none" stroke="#fff" stroke-width="4"/></svg>
<svg class="abs arrow" style="left:1064px" width="24" height="40" viewBox="0 0 24 40"><path d="M4 4l14 16L4 36" fill="none" stroke="#fff" stroke-width="4"/></svg>

<footer class="abs site-footer"></footer>
<div class="abs footer-brand">Kesta furniture</div>

<div class="abs links">
  <div class="foot-title">Links</div>
  <ul><li>Home</li><li>About</li><li>Shop</li><li>Products</li><li>My Account</li><li>Shipping &amp; Delivery</li><li>FAQ's</li></ul>
</div>

<div class="abs contact">
  <div class="foot-title">Contact Us</div>
  <div class="contact-row"><span class="dot"><svg width="14" height="18" viewBox="0 0 14 18"><path d="M7 17S1 10 1 6.5a6 6 0 0 1 12 0C13 10 7 17 7 17z" fill="#fff"/><circle cx="7" cy="6.5" r="2.2" fill="var(--teal)"/></svg></span><span>Location Name<br>Harrow Lane 12<br>Brenton 7310 KL 58261</span></div>
  <div class="contact-row"><span class="dot"><svg width="16" height="16" viewBox="0 0 16 16"><path d="M3 1l3 3-2 2c1 2 4 5 6 6l2-2 3 3-2 2C7 15 1 9 1 3z" fill="#fff"/></svg></span><span style="padding-top:8px">Phone:020 48 31706</span></div>
  <div class="contact-row"><span class="dot"><svg width="16" height="12" viewBox="0 0 16 12"><rect x="1" y="1" width="14" height="10" fill="#fff"/><path d="M1 1l7 6 7-6" fill="none" stroke="var(--teal)" stroke-width="1.4"/></svg></span><span style="padding-top:8px">Email:hello@kestahome.com</span></div>
</div>

<div class="abs newsletter">
  <div class="foot-title">Newsletter Sign up</div>
  <p>Lorem ipsum dolor sit amet consec tetur adipiscing elit sed do eiusmod</p>
  <div class="email">Email
    <span class="go"><svg width="14" height="14" viewBox="0 0 14 14"><path d="M1 7h11M8 3l4 4-4 4" fill="none" stroke="#fff" stroke-width="2"/></svg></span>
  </div>
  <div class="social"><span></span><span></span><span></span><span></span></div>
</div>

<div class="abs bottom-bar"></div>
<div class="abs copyright">© 2022 All Rights Reserved Terms &amp; Conditions Privacy Policy</div>
<div class="abs payments"><span></span><span></span><span></span><span></span><span></span><span></span></div>

</body>
</html>
```